High Quality Business card for Property Management Agency - Super Classy and professional design

High Quality Business card design.

We need a business card designed for our Property Management Agency.
We are located on Sydney's Northern Beaches and manage beautiful properties along the beach and harbor.
We need a design that oozes modern, classy and professional.
I would like it to be double sided with contact details and logo on the front and just the logo on the back.

I need a print ready PDF version of the file as well as an editable photoshop (PSD) version of the file.

Logo and information details attached.

Target Market(s)

Property owners/investors, Male and Female Aged 28-65

Industry/Entity Type

Real Estate

Contact Information for Business Card

Tom Harlow
Tel: 0437 216 590
Email: tom@harlowestates.com.au
Website: www.harlowestates.com.au
Address: Level 2, 17 Kestrel Rd, Wendale NSW 2081

Font styles to use
Sans Serif

Requirements
Must have
• - Logo front and back
• - Business card details listed above and attached
• - Colour
Nice to have
• Sleek and professional

```html
<!DOCTYPE html>
<html lang="en">
<head>
<meta charset="utf-8">
<title>Harlow Estates – Business Card</title>
<link href="https://fonts.googleapis.com/css2?family=Arimo:wght@400;700&display=swap" rel="stylesheet">
<style>
  :root {
    --stage: #3a3a3a;
    --card-white: #ffffff;
    --card-black: #1c1c1c;
    --plate-light: #2e2e2e;
    --plate-dark: #161616;
    --teal: #2a9ba3;
    --ink: #1e1e1e;
    --grey: #555555;
    --rule: #9a9a9a;
  }
  * { margin: 0; padding: 0; box-sizing: border-box; }
  html, body {
    width: 1200px; height: 913px; overflow: hidden;
    background: var(--stage);
    font-family: "Arimo", Arial, sans-serif;
  }
  .stage {
    width: 1200px; height: 913px;
    display: flex; align-items: center; justify-content: center; gap: 30px;
  }
  .card {
    position: relative;
    width: 560px; height: 320px;
    overflow: hidden;
    box-shadow: 0 14px 30px rgba(0,0,0,.45);
  }
  /* Back */
  .card-back { background: var(--card-black); }
  .plate-texture {
    position: absolute; inset: 0;
    background: linear-gradient(135deg, var(--plate-light), var(--plate-dark));
  }
  .brand {
    position: absolute;
    display: flex; align-items: center; gap: 10px;
    font-weight: 700; text-transform: uppercase; letter-spacing: .5px;
    white-space: nowrap;
  }
  .brand-mark { width: 14px; height: 14px; background: var(--teal); }
  .card-back .brand { right: 44px; top: 140px; font-size: 30px; color: #ffffff; }
  /* Front */
  .card-front { background: var(--card-white); color: var(--ink); }
  .card-front .brand { right: 34px; top: 42px; font-size: 30px; color: var(--ink); }
  .brand-rule {
    position: absolute; left: 190px; right: 20px; top: 104px;
    height: 1px; background: var(--rule);
  }
  .contact { position: absolute; left: 34px; top: 152px; width: 320px; }
  .contact-name {
    font-size: 22px; font-weight: 700; color: var(--teal);
    text-transform: uppercase; letter-spacing: .5px;
  }
  .name-rule { width: 200px; height: 1px; background: var(--rule); margin: 8px 0 10px; }
  .address { font-size: 13px; line-height: 17px; color: var(--grey); }
  .lines { list-style: none; margin-top: 10px; }
  .lines li {
    display: flex; align-items: center; gap: 8px;
    font-size: 13px; line-height: 20px; color: var(--grey);
  }
  .lines li.phone { font-weight: 700; font-size: 15px; color: var(--ink); }
  .icon { width: 12px; height: 12px; flex: none; }
</style>
</head>
<body>
<main class="stage">
  <section class="card card-back" aria-label="Card back">
    <div class="plate-texture" role="img" aria-label="Dark diamond-plate pattern"></div>
    <div class="brand"><span class="brand-mark"></span>Harlow Estates</div>
  </section>

  <section class="card card-front" aria-label="Card front">
    <div class="brand"><span class="brand-mark"></span>Harlow Estates</div>
    <div class="brand-rule"></div>
    <div class="contact">
      <p class="contact-name">Tom Harlow</p>
      <div class="name-rule"></div>
      <p class="address">Level 2, 17 Kestrel Rd<br>Wendale NSW 2081</p>
      <ul class="lines">
        <li class="phone">
          <svg class="icon" viewBox="0 0 12 12"><path d="M3 1 L5 3.5 L4 5 Q5 7 7 8 L8.5 7 L11 9 L9.5 11 Q5 11 2.5 8 Q0.5 5 1 2.5 Z" fill="var(--teal)"/></svg>
          0437 216 590
        </li>
        <li>
          <svg class="icon" viewBox="0 0 12 12"><rect x="1" y="2.5" width="10" height="7" rx="1" fill="var(--teal)"/><path d="M1.5 3 L6 6.5 L10.5 3" stroke="#fff" fill="none"/></svg>
          tom@harlowestates.com.au
        </li>
        <li>
          <svg class="icon" viewBox="0 0 12 12"><circle cx="6" cy="6" r="5" fill="none" stroke="var(--teal)" stroke-width="1.4"/><path d="M1 6 H11 M6 1 Q3 6 6 11 Q9 6 6 1" fill="none" stroke="var(--teal)"/></svg>
          www.harlowestates.com.au
        </li>
      </ul>
    </div>
  </section>
</main>
</body>
</html>
```